Web design - Submit your captivating design
4 simple captivating pages
Web design - Submit your captivating design - Education
Creative Brief
Education
We provide affordable easily understandable innovative solutions that will enable students enjoy rapid, sustained and consistent success in the math and sciences.
Blue
Brown
top
Nav placement is up to your design. Colors should be the colors of the logo. Pages - Front page, activity page, contact us and about us page.

```html
<!DOCTYPE html>
<html lang="en">
<head>
<meta charset="utf-8">
<title>RedFerns – Contact Us</title>
<link href="https://fonts.googleapis.com/css2?family=Arimo:wght@400;700&display=swap" rel="stylesheet">
<style>
:root{
  --orange:#f7941d;
  --orange-dark:#e07c0c;
  --blue:#2d9bd8;
  --blue-light:#5bb8ea;
  --text:#444;
  --muted:#666;
  --line:#d8d8d8;
  --footer:#e3e3e3;
  --footer-dark:#5a5a5a;
  --white:#fff;
}
*{margin:0;padding:0;box-sizing:border-box}
html,body{width:1200px;height:929px;overflow:hidden}
body{font-family:"Arimo",Arial,sans-serif;color:var(--text);background:var(--white);position:relative}
.abs{position:absolute}

.site-header{position:absolute;left:0;top:0;width:1200px;height:132px;background:linear-gradient(#fff,#f1f1f1)}
.brand{left:162px;top:34px;display:flex;align-items:center;gap:14px}
.brand-mark{width:58px;height:58px;border-radius:50%;background:var(--blue)}
.brand-name{font-size:54px;font-weight:700;color:var(--orange);letter-spacing:-1px}
.account-links{left:962px;top:24px;font-size:12px;color:#333}
.account-links span{margin:0 6px;color:#999}
.header-phone{left:878px;top:66px;font-size:22px;color:#333;display:flex;align-items:center;gap:8px}

.blue-band{left:0;top:132px;width:1200px;height:64px;background:linear-gradient(var(--blue-light),var(--blue))}
.main-nav{left:160px;top:132px;width:880px;height:48px;background:linear-gradient(#fbab43,var(--orange));display:flex;align-items:center;padding-left:6px;box-shadow:0 2px 3px rgba(0,0,0,.2)}
.main-nav a{color:#fff;text-decoration:none;font-size:16px;padding:0 16px;height:48px;line-height:48px;border-right:1px solid rgba(255,255,255,.45)}
.main-nav a.active{background:var(--blue);border:2px solid #fff;height:40px;line-height:36px;margin-left:12px}
.search{position:absolute;right:10px;top:11px;width:186px;height:26px;background:#fff;border:1px solid #ddd;font-size:12px;color:#555;padding:5px 8px}
.search svg{position:absolute;right:6px;top:4px}

.page-strip{left:0;top:196px;width:1200px;height:70px;background:linear-gradient(#f5f5f5,#fff)}
.page-title{left:160px;top:226px;font-size:19px;font-weight:400;color:var(--orange)}
.divider{left:160px;top:262px;width:880px;height:1px;background:var(--line)}
.notch{left:588px;top:262px;width:0;height:0;border-left:12px solid transparent;border-right:12px solid transparent;border-top:8px solid var(--line)}
.intro{left:160px;top:284px;width:880px;font-size:11.5px;line-height:16px;color:#555}

.form-panel{left:160px;top:340px;width:390px;height:365px;background:#fff;box-shadow:0 0 6px rgba(0,0,0,.22);border-radius:3px}
.form-tab{left:150px;top:357px;width:396px;height:34px;background:var(--orange);color:#fff;font-size:15px;line-height:34px;padding-left:26px}
.tab-fold{left:150px;top:391px;width:0;height:0;border-top:8px solid var(--orange-dark);border-left:10px solid transparent}
.field-label{left:188px;font-size:12px;color:#444}
.field{left:265px;width:255px;height:28px;border:1px solid #bbb;background:#fff}
.select{font-size:11px;padding:6px 8px;color:#444}
.select svg{position:absolute;right:8px;top:9px}
.textarea{height:118px}
.submit{left:265px;top:662px;width:90px;height:28px;background:var(--orange);color:#fff;font-size:15px;text-align:center;line-height:28px}

.contact-info{left:688px;top:442px;width:320px}
.contact-info h2{font-weight:400;font-size:20px;color:var(--orange);margin-bottom:10px}
.contact-info p{font-size:15px;line-height:19px;color:#555}
.contact-info .row{font-size:17px;color:#222;margin-top:6px}
.contact-info .row b{font-weight:700;color:var(--orange);display:inline-block;width:64px;font-size:15px}

.site-footer{left:0;top:732px;width:1200px;height:156px;background:var(--footer)}
.footer-col{top:742px}
.footer-col h3{font-weight:400;font-size:14.5px;color:var(--orange);margin-bottom:12px}
.footer-col li{list-style:none;font-size:11.5px;color:#333;margin-bottom:14px}
.vsep{top:744px;width:1px;height:128px;background:#c9c9c9}
.social li{display:flex;justify-content:space-between;align-items:center;width:100px;margin-bottom:8px}
.social .sq{width:20px;height:20px;background:var(--blue);display:inline-block}
.email-box{width:174px;height:24px;background:#fff;border:1px solid #bbb;font-size:10.5px;color:#888;padding:5px 6px;margin-bottom:10px}
.note{font-size:10.5px;color:#333;margin-bottom:8px}
.signup{width:62px;height:22px;background:var(--orange);color:#fff;font-size:12px;text-align:center;line-height:22px}
.footer-brand{left:808px;top:768px;display:flex;align-items:center;gap:10px}
.footer-brand .brand-mark{width:46px;height:46px;background:#8a8a8a}
.footer-brand .brand-name{font-size:44px;color:#777}
.bottom-bar{left:0;top:888px;width:1200px;height:41px;background:var(--footer-dark);color:#fff;font-size:11px;line-height:41px}
.bottom-bar .legal{position:absolute;left:162px}
.bottom-bar .copy{position:absolute;right:160px}
</style>
</head>
<body>
<header class="site-header">
  <div class="abs brand"><span class="brand-mark"></span><span class="brand-name">RedFerns</span></div>
  <div class="abs account-links">Login<span>|</span>Signup</div>
  <div class="abs header-phone">
    <svg width="20" height="16" viewBox="0 0 20 16"><path d="M2 6c0-3 4-4 8-4s8 1 8 4l-3 1-1-2H6L5 7z" fill="#333"/><rect x="4" y="8" width="12" height="7" rx="1" fill="#333"/></svg>
    555 - 555 - 555
  </div>
</header>

<div class="abs blue-band"></div>
<nav class="abs main-nav">
  <a href="#">Home</a><a href="#">About RedFerns</a><a href="#">RedFerns' Programs</a><a href="#">How it works</a><a href="#" class="active">Contact Us</a>
  <div class="search">Search
    <svg width="16" height="16" viewBox="0 0 16 16"><circle cx="6.5" cy="6.5" r="4.5" fill="none" stroke="#444" stroke-width="2"/><path d="M10 10l4.5 4.5" stroke="#444" stroke-width="2.4"/></svg>
  </div>
</nav>

<div class="abs page-strip"></div>
<h1 class="abs page-title">Contact Us</h1>
<div class="abs divider"></div>
<div class="abs notch"></div>
<p class="abs intro">Lorem ipsum dolor sit amet, consectetur adipisicing elit, sed do eiusmod tempor incididunt ut labore et dolore magna aliqua. Ut enim ad minim veniam, quis nostrud exercitation ullamco laboris nisi ut aliquip ex ea commodo consequat duis aute irure dolor in reprehenderit.</p>

<section>
  <div class="abs form-panel"></div>
  <div class="abs form-tab">Fill Up The Form Below</div>
  <div class="abs tab-fold"></div>
  <span class="abs field-label" style="top:412px">Name :</span>
  <div class="abs field" style="top:405px"></div>
  <span class="abs field-label" style="top:455px">Interested in :</span>
  <div class="abs field select" style="top:447px">Select Programs
    <svg width="10" height="8" viewBox="0 0 10 8"><path d="M0 0h10L5 8z" fill="#333"/></svg>
  </div>
  <span class="abs field-label" style="top:497px">Email ID :</span>
  <div class="abs field" style="top:490px"></div>
  <span class="abs field-label" style="top:535px">Detail :</span>
  <div class="abs field textarea" style="top:530px"></div>
  <div class="abs submit">Submit</div>
</section>

<section class="abs contact-info">
  <h2>RedFerns (Learn To Grow)</h2>
  <p>000, Lorem ipsum dolor sit amet,<br>consectetur adipisLorem ipsum<br>dolor sit amet, 00.000.</p>
  <div class="row" style="margin-top:12px"><b>Phone :</b>555 - 555 - 555</div>
  <div class="row"><b>Email :</b>info@redferns.com</div>
</section>

<footer>
  <div class="abs site-footer"></div>
  <div class="abs footer-col" style="left:162px">
    <h3>Quick Links</h3>
    <ul><li>Home</li><li>About RedFerns</li><li>RedFerns' Programs</li><li>How it works</li></ul>
  </div>
  <div class="abs vsep" style="left:296px"></div>
  <div class="abs footer-col social" style="left:316px">
    <h3>Share and Get Connected</h3>
    <ul>
      <li>Chatterly<span class="sq"></span></li>
      <li>Birdcall<span class="sq"></span></li>
      <li>Workline<span class="sq"></span></li>
    </ul>
  </div>
  <div class="abs vsep" style="left:540px"></div>
  <div class="abs footer-col" style="left:563px">
    <h3>Newsletter</h3>
    <div class="email-box">Enter Your Email Address</div>
    <p class="note">Signup for get our Updated Newsletter!</p>
    <div class="signup">Signup</div>
  </div>
  <div class="abs vsep" style="left:776px"></div>
  <div class="abs footer-brand"><span class="brand-mark"></span><span class="brand-name">RedFerns</span></div>
  <div class="abs bottom-bar"><span class="legal">Terms of Use &nbsp;|&nbsp; Privacy Statement</span><span class="copy">Copyright © 2012</span></div>
</footer>
</body>
</html>
```